CD design for very cool music project

I need some stunning artwork for physical/digital CD cover. I already have all the art submitted by a fan that I want to use pretty much exactly the same, but done professionally and high quality/resolution. Basically deconstructing the current art and remaking it awesome. I also have the band logo and name for the CD completed that I want incorporated into the art. Should be an EXTREMELY EASY project.

Requirements
Must have
• All the elements in the images I submitted. There are stars and cosmic type imagery as sand in the hourglass as well as the DNA strands in the background. The Hunab Ku mayan symbol in the top of the hourglass and all the original elements present in the image I submitted.
• Also, the Talbot's Lantern logo has to be horizontal and include the T and L logo (included in the brief).
Nice to have
• The CD is called "9 Rivers" so I'd like to see heavy metal styled entries (like for the word "Rivers" some cool font consitent with the Talbot's Lantern logo but with moons for the O's or something cool along those lines.
Should not have
• Any colours aside from the ones included. The stars and cosmos "sand" can be colorful like Vantor space images, galaxies and stars would look like. It can't be cartoonie in any way as the music is dark and serious.

```html
<!DOCTYPE html>
<html lang="en">
<head>
<meta charset="utf-8">
<title>9 Rivers — Talbot's Lantern</title>
<link rel="stylesheet" href="https://fonts.googleapis.com/css2?family=Cormorant+Garamond:wght@300;400&family=Raleway:wght@200;600&display=swap">
<style>
  :root {
    --night: #07070d;
    --deep: #141627;
    --violet: #3a3a9a;
    --glow: #5a55d6;
    --silver: #d9dce4;
    --silver-dark: #7d818c;
    --frame: rgba(220, 222, 230, 0.55);
    --white: #f2f3f6;
  }
  * { margin: 0; padding: 0; box-sizing: border-box; }
  html, body {
    width: 1200px;
    height: 1200px;
    overflow: hidden;
    background: var(--night);
  }
  .cover {
    position: relative;
    width: 1200px;
    height: 1200px;
    overflow: hidden;
  }
  .cosmic-artwork {
    position: absolute;
    inset: 0;
    background:
      radial-gradient(ellipse 110px 260px at 50% 33%, rgba(90, 85, 214, 0.55), transparent 70%),
      radial-gradient(ellipse 130px 160px at 50% 85%, rgba(70, 70, 170, 0.55), transparent 70%),
      radial-gradient(ellipse 260px 520px at 50% 50%, rgba(120, 125, 150, 0.22), transparent 75%),
      radial-gradient(circle at 50% 45%, #1c1f33 0%, var(--deep) 40%, var(--night) 85%);
  }
  .hourglass-glass {
    position: absolute;
    left: 430px;
    top: 0;
    width: 340px;
    height: 1200px;
    border-radius: 48% / 22%;
    background:
      linear-gradient(90deg, rgba(200, 205, 225, 0.14), transparent 22%, transparent 78%, rgba(200, 205, 225, 0.14));
  }
  .frame {
    position: absolute;
    left: 40px;
    right: 40px;
    top: 47px;
    bottom: 36px;
    border: 1.5px solid var(--frame);
  }
  .emblem {
    position: absolute;
    left: 524px;
    top: 54px;
    width: 152px;
    height: 152px;
    border-radius: 50%;
    background: radial-gradient(circle at 45% 40%, #e6e7ea, #b7b9bf 70%, #8d9097);
    box-shadow: 0 0 0 3px #1b1b22;
  }
  .title {
    position: absolute;
    left: 0;
    right: 0;
    text-align: center;
  }
  .title-number {
    top: 410px;
    font-family: "Cormorant Garamond", serif;
    font-weight: 400;
    font-size: 300px;
    line-height: 1;
    background: linear-gradient(180deg, var(--white) 0%, var(--silver-dark) 45%, var(--silver) 60%, #555963 100%);
    -webkit-background-clip: text;
    background-clip: text;
    color: transparent;
  }
  .title-word {
    top: 700px;
    font-family: "Raleway", sans-serif;
    font-weight: 200;
    font-size: 190px;
    line-height: 1;
    letter-spacing: 6px;
    background: linear-gradient(180deg, var(--white) 0%, var(--silver) 55%, var(--silver-dark) 100%);
    -webkit-background-clip: text;
    background-clip: text;
    color: transparent;
  }
  .band-name {
    position: absolute;
    left: 0;
    right: 0;
    top: 1048px;
    display: flex;
    justify-content: center;
    align-items: center;
    gap: 28px;
    font-family: "Raleway", sans-serif;
    font-weight: 600;
    font-size: 28px;
    letter-spacing: 10px;
    color: var(--white);
    text-transform: uppercase;
  }
  .band-dot {
    width: 16px;
    height: 16px;
    border-radius: 50%;
    background: var(--white);
  }
</style>
</head>
<body>
  <main class="cover">
    <div class="cosmic-artwork" role="img" aria-label="Dark cosmic scene with molecular DNA strands and a glass hourglass filled with starry violet galaxy sand"></div>
    <div class="hourglass-glass" aria-hidden="true"></div>
    <div class="frame" aria-hidden="true"></div>
    <div class="emblem" role="img" aria-label="Mayan galactic-centre emblem at the top of the hourglass"></div>
    <h1 class="title title-number">9</h1>
    <p class="title title-word">RIVERS</p>
    <p class="band-name"><span>Talbot's</span><span class="band-dot"></span><span>Lantern</span></p>
  </main>
</body>
</html>
```